New Business Card for our Indoor Golf Training Facility

We are looking for designs for a new business card for our indoor golf training facility. Attached is our logo, our logo with our slogan, and here is our elevator pitch (What makes us different from the others) not sure if all the info will fit on one card, maybe you can condense the elevator pitch? here is the info

Elevator Pitch
We work with serious golfers and those that want to be serious golfers…
to make you better, faster, at all phases of the game…
We use the same state-of-the-art technology as professional golfers…
which produces data sets that shows your improvement in real time.
Our facility is available 24/7 to our members, which allows you to improve on your time.

our website: www.brambleteegolf.com

Target Market(s)

Golfers

Font styles to use
Serif
Sans Serif

Colors
ec1f27
f59195
fbd4d5
919191
d3d3d3
1b1b1b

Requirements
Must have
• our logo or our logo with the slogan, elevator pitch (can be condensed or shortened)

```html
<!DOCTYPE html>
<html lang="en">
<head>
<meta charset="utf-8">
<title>Bramble Tee Golf – Business Card</title>
<link rel="stylesheet" href="https://fonts.googleapis.com/css2?family=Montserrat:wght@400;700&family=Lato:wght@300;400;700&display=swap">
<style>
  :root {
    --red: #ec1f27;
    --red-card: #e23a33;
    --pink: #f59195;
    --blush: #fbd4d5;
    --grey: #919191;
    --light-grey: #d3d3d3;
    --ink: #1b1b1b;
    --paper: #f4f4f4;
    --backdrop: #c9c9c9;
  }
  * { box-sizing: border-box; margin: 0; padding: 0; }
  html, body { width: 1200px; height: 960px; overflow: hidden; }
  body {
    background: var(--backdrop);
    font-family: "Lato", sans-serif;
    position: relative;
  }
  .card {
    position: absolute;
    width: 700px;
    height: 400px;
    overflow: hidden;
    box-shadow: 0 6px 18px rgba(0,0,0,0.18);
  }

  /* Back side */
  .card--back { left: 250px; top: 60px; background: var(--red-card); }
  .card--back .band {
    position: absolute; left: 0; width: 100%; height: 22px;
    background: var(--light-grey);
  }
  .band--top { top: 120px; }
  .band--bottom { top: 344px; }
  .pitch-title {
    position: absolute; left: 60px; top: 154px;
    font-family: "Montserrat", sans-serif; font-weight: 700;
    font-size: 17px; color: var(--blush); letter-spacing: 0.5px;
  }
  .pitch-list {
    position: absolute; left: 40px; top: 184px; right: 40px;
    list-style: none; color: #fff; font-size: 14.5px; line-height: 29px;
  }
  .pitch-list li { position: relative; padding-left: 20px; }
  .pitch-list li::before {
    content: ""; position: absolute; left: 0; top: 10px;
    width: 8px; height: 8px; border: 2px solid var(--light-grey);
    border-radius: 50%;
  }

  /* Front side */
  .card--front { left: 250px; top: 500px; background: var(--paper); }
  .brand {
    position: absolute; left: 34px; top: 30px;
    display: flex; align-items: center; gap: 12px;
  }
  .brand-dot {
    width: 40px; height: 40px; border: 4px solid var(--red); border-radius: 50%;
  }
  .brand-name {
    font-family: "Montserrat", sans-serif; font-weight: 700;
    font-size: 40px; color: var(--red); line-height: 1;
  }
  .slogan {
    position: absolute; left: 86px; top: 82px;
    font-family: "Lato", sans-serif; font-weight: 300;
    font-size: 16px; color: var(--red);
  }
  .name-band {
    position: absolute; left: 320px; top: 128px; width: 380px; height: 86px;
    background: var(--red); text-align: right; padding: 12px 34px 0 0;
  }
  .person-name {
    font-family: "Montserrat", sans-serif; font-weight: 400;
    font-size: 32px; color: var(--light-grey); letter-spacing: 1px; line-height: 1.1;
  }
  .person-role {
    font-family: "Lato", sans-serif; font-size: 17px; color: var(--blush);
  }
  .contacts {
    position: absolute; right: 30px; top: 236px;
    list-style: none; color: #3a3a3a; font-size: 17px;
  }
  .contacts li {
    display: flex; align-items: center; justify-content: flex-end;
    gap: 14px; height: 36px; text-align: right;
  }
  .contacts .address { height: auto; padding-top: 4px; line-height: 22px; }
  .icon { width: 28px; height: 28px; flex: none; }
</style>
</head>
<body>

<section class="card card--back" aria-label="Card back">
  <div class="band band--top"></div>
  <h2 class="pitch-title">Elevator Pitch</h2>
  <ul class="pitch-list">
    <li>We work with serious golfers and those that want to be serious golfers…</li>
    <li>to make you better, faster, at all phases of the game…</li>
    <li>We use the same state-of-the-art technology as professional golfers…</li>
    <li>which produces data sets that shows your improvement in real time.</li>
    <li>Our facility is available 24/7 to our members, which allows you to improve on your time</li>
  </ul>
  <div class="band band--bottom"></div>
</section>

<section class="card card--front" aria-label="Card front">
  <div class="brand">
    <span class="brand-dot"></span>
    <span class="brand-name">Bramble Tee Golf</span>
  </div>
  <p class="slogan">Par Is Good. Better Is Better.</p>

  <div class="name-band">
    <p class="person-name">DANIEL REYES</p>
    <p class="person-role">Founder &amp; CEO</p>
  </div>

  <ul class="contacts">
    <li>+34 900 412 386
      <svg class="icon" viewBox="0 0 28 28" aria-hidden="true"><circle cx="14" cy="14" r="14" fill="var(--red)"/><path d="M10 8c1 0 2 2 2 3s-1 1-1 2 3 4 4 4 1-1 2-1 3 1 3 2-1 2-2 2c-4 0-10-6-10-10 0-1 1-2 2-2z" fill="#fff"/></svg>
    </li>
    <li>info@brambleteegolf.com
      <svg class="icon" viewBox="0 0 28 28" aria-hidden="true"><circle cx="14" cy="14" r="14" fill="var(--red)"/><rect x="7" y="9" width="14" height="10" fill="none" stroke="#fff" stroke-width="1.6"/><path d="M7 9l7 6 7-6" fill="none" stroke="#fff" stroke-width="1.6"/></svg>
    </li>
    <li>www.brambleteegolf.com
      <svg class="icon" viewBox="0 0 28 28" aria-hidden="true"><circle cx="14" cy="14" r="14" fill="var(--red)"/><g fill="none" stroke="#fff" stroke-width="1.4"><circle cx="14" cy="14" r="7"/><ellipse cx="14" cy="14" rx="3" ry="7"/><path d="M7 14h14M8.5 10.5h11M8.5 17.5h11"/></g></svg>
    </li>
    <li class="address"><span>Calle del Prado 14, Oficina 2B<br>24001, Valdecruz</span>
      <svg class="icon" viewBox="0 0 28 28" aria-hidden="true"><circle cx="14" cy="14" r="14" fill="var(--red)"/><path d="M14 6a5 5 0 0 1 5 5c0 4-5 10-5 10s-5-6-5-10a5 5 0 0 1 5-5z" fill="#fff"/><circle cx="14" cy="11" r="2" fill="var(--red)"/></svg>
    </li>
  </ul>
</section>

</body>
</html>
```